Landscape Supplier and Excavation company needing a website revamp.

We need a web design for our company based out of northern Virginia. We make and deliver topsoil, mulch, and compost. We are also an excavation company. We provide a wide variety of excavation services, from residential to large commercial projects. We specialize in land clearing and building site preparation. We would like a site that looks very professional and makes us look like a large company. We've been in business since 1994 and have never had a really nice website. Our current website it www.harrowfieldloam.com and www.pvrqx.com for references. I like the information on the pages but would like something more professional looking. Doesn't HAVE to be 4 different pages, but I would like a contact form, our services, and our products/ pricing listed. We are properly licensed and insured and would like this included somewhere on the site.

Target Market(s)

Landscapers, Home Owners, Commercial

Industry/Entity Type

Excavation and Landscape Products Supplier

Number of Pages Required

4 page

Colors

Designer to choose colors to be used in the design.

Requirements
Must have
• Professional Look and Feel

```html
<!DOCTYPE html>
<html lang="en">
<head>
<meta charset="utf-8">
<title>Harrowfield Loam and Excavation</title>
<link href="https://fonts.googleapis.com/css2?family=Oswald:wght@300;400;500;700&family=Lato:ital,wght@0,400;0,700;1,400&display=swap" rel="stylesheet">
<style>
:root{
  --backdrop:#f6dcdc;
  --red:#c1282d;
  --red-dark:#6d0a0c;
  --ink:#111;
  --black:#141414;
  --cream:#faf8f4;
  --white:#fff;
  --grey:#555;
  --line:#2e2e2e;
  --light-line:#ddd;
  --hero:linear-gradient(115deg,#3a3a3a 0%,#2c2c2c 38%,#5a3a32 60%,#93291f 76%,#3b3b3b 100%);
}
*{box-sizing:border-box;margin:0;padding:0}
html,body{width:1200px;height:3750px;overflow:hidden;background:var(--backdrop)}
body{font-family:"Lato",sans-serif;color:var(--ink);position:relative}
.head{font-family:"Oswald",sans-serif;text-transform:uppercase;font-weight:500}
.eyebrow{font-family:"Lato",sans-serif;text-transform:uppercase;color:var(--red);letter-spacing:2px}
.btn{display:inline-block;background:var(--red);color:#fff;font-family:"Oswald",sans-serif;text-transform:uppercase;letter-spacing:.4px}
.abs{position:absolute}

/* showcase title */
.show-brand{position:absolute;top:206px;left:0;width:1200px;text-align:center;font-family:"Oswald",sans-serif;font-weight:700;font-size:46px;letter-spacing:2px;color:var(--red);text-transform:uppercase}

/* side labels */
.side-label{position:absolute;font-family:"Oswald",sans-serif;font-weight:300;font-size:17px;letter-spacing:11px;color:var(--red);text-transform:uppercase;white-space:nowrap;transform:rotate(-90deg);transform-origin:center}
.side-label.left{left:-20px;top:2230px;width:250px;text-align:center}
.side-label.right{left:966px;top:2280px;width:250px;text-align:center}

/* flat screen previews */
.preview-desk{position:absolute;left:262px;top:372px;width:742px;height:463px;background:var(--hero);overflow:hidden}
.preview-desk .p-notice{height:13px;background:var(--red-dark);color:#fff;font-size:5px;text-align:center;line-height:13px;text-transform:uppercase}
.preview-desk .p-header{height:57px;background:var(--cream);position:relative}
.preview-desk .p-brand{position:absolute;left:98px;top:17px;font-family:"Oswald",sans-serif;font-weight:700;font-size:16px;color:var(--red);text-transform:uppercase}
.preview-desk .p-nav{position:absolute;right:100px;top:23px;display:flex;gap:18px;font-family:"Oswald",sans-serif;font-size:7.5px;text-transform:uppercase}
.preview-desk .p-nav .on{color:var(--red)}
.p-hero{position:absolute;left:0;width:100%;text-align:center;color:#fff}
.preview-desk .p-hero{top:126px}
.preview-desk .p-eyebrow{font-size:8px;letter-spacing:3px;color:#eee;text-transform:uppercase}
.preview-desk h2{font-size:28px;margin:6px 0 18px}
.preview-desk p{font-size:8.5px;line-height:1.95}
.preview-desk .btn{font-size:7.5px;padding:8px 14px;margin-top:16px}

.preview-phone{position:absolute;left:140px;top:579px;width:167px;height:298px;background:var(--hero);overflow:hidden;border:1px solid #333}
.preview-phone .p-header{height:40px;background:#fff;position:relative}
.preview-phone .p-brand{position:absolute;left:14px;top:13px;font-family:"Oswald",sans-serif;font-weight:700;font-size:9.5px;color:var(--red);text-transform:uppercase}
.burger{position:absolute;display:flex;flex-direction:column;justify-content:space-between}
.burger i{display:block;height:1px;background:var(--red)}
.preview-phone .burger{right:14px;top:16px;width:10px;height:8px}
.preview-phone .p-hero{top:80px;padding:0 10px}
.preview-phone h2{font-size:12.5px;line-height:1.5}
.preview-phone p{font-size:6px;line-height:1.7;margin-top:12px}
.preview-phone .btn{font-size:5.5px;padding:5px 9px;margin-top:12px}

/* ============ DESKTOP PAGE (1000 wide, scaled) ============ */
.desk{position:absolute;left:358px;top:945px;width:1000px;height:3737px;transform:scale(.698);transform-origin:0 0;background:#fff;overflow:hidden}
.desk .notice{position:absolute;top:0;left:0;width:1000px;height:23px;background:var(--red-dark);color:#fff;font-size:8px;text-align:center;line-height:23px;letter-spacing:.3px;text-transform:uppercase}
.desk .site-header{position:absolute;top:23px;left:0;width:1000px;height:81px;background:var(--cream)}
.desk .brand{position:absolute;left:134px;top:25px;font-family:"Oswald",sans-serif;font-weight:700;font-size:22px;color:var(--red);text-transform:uppercase;letter-spacing:.5px}
.desk .nav{position:absolute;right:134px;top:32px;display:flex;gap:26px;font-family:"Oswald",sans-serif;font-size:10px;text-transform:uppercase}
.desk .nav .active{color:var(--red);border-bottom:2px solid var(--red);padding-bottom:3px}

.desk .hero{position:absolute;top:104px;left:0;width:1000px;height:658px;background:var(--hero)}
.desk .hero-content{position:absolute;top:155px;left:0;width:1000px;text-align:center;color:#fff}
.desk .hero-content .eyebrow{color:#eee;letter-spacing:4px;font-size:11px}
.desk .hero-content h1{font-size:38px;margin:12px 0 24px;font-weight:500}
.desk .hero-content p{font-size:12.5px;line-height:1.8}
.desk .hero-content .btn{margin-top:22px;font-size:11px;padding:12px 22px}

.desk .product-tiles{position:absolute;top:679px;left:134px;width:730px;height:173px;display:flex;gap:10px;padding:7px;background:#fff;box-shadow:0 6px 16px rgba(0,0,0,.15)}
.tile{flex:1;background:var(--black)}
.tile .label{color:#fff;text-align:center;font-family:"Oswald",sans-serif;text-transform:uppercase}
.tile .label span{color:var(--red);margin-left:10px}
.desk .tile .photo{height:123px}
.desk .tile .label{height:36px;line-height:36px;font-size:11px}

.desk .about{position:absolute;top:762px;left:0;width:1000px;height:587px}
.desk .about-photo{position:absolute;left:134px;top:171px;width:336px;height:341px;background:linear-gradient(#6f8a5a,#c9cccc 55%,#777);border:5px solid #eee;box-shadow:0 2px 8px rgba(0,0,0,.2)}
.desk .about-text{position:absolute;left:509px;top:171px;width:355px}
.desk .about-text .eyebrow{font-size:9px}
.desk .about-text h2{font-size:24px;margin:4px 0 14px}
.desk .about-text p{font-size:10.5px;line-height:1.75;color:var(--grey);margin-bottom:13px}
.quote{color:var(--red) !important;font-style:italic}
.about-cta{display:flex;align-items:center;gap:18px;margin-top:20px}
.call{font-family:"Oswald",sans-serif;color:#777;text-transform:uppercase;line-height:1.5}
.call b{color:var(--ink);font-weight:500}
.desk .about-cta .btn{font-size:10px;padding:12px 20px}
.desk .call{font-size:10px}
.desk .call b{font-size:12px}

.desk .services{position:absolute;top:1349px;left:0;width:1000px;height:659px;background:radial-gradient(circle at 50% 40%,#2e2d2a,#191817)}
.section-title{text-align:center;color:#fff}
.desk .section-title{padding-top:73px}
.desk .section-title .eyebrow{font-size:9px}
.desk .section-title h2{font-size:26px;margin:4px 0 14px}
.desk .section-title p{font-size:10px;line-height:1.8;color:#aaa;width:500px;margin:0 auto}
.desk .service-cards{position:absolute;top:202px;left:134px;width:730px;display:flex;gap:19px}
.service{flex:1;background:#fff;text-align:center;position:relative}
.service .icon{position:absolute;left:50%;border-radius:50%;background:var(--red);border:3px solid #fff;display:flex;align-items:center;justify-content:center}
.desk .service{height:324px}
.desk .service .photo{height:140px}
.desk .service .icon{top:115px;width:50px;height:50px;margin-left:-25px}
.desk .service h3{font-size:14px;margin-top:40px}
.desk .service p{font-size:10px;line-height:1.8;color:var(--grey);padding:10px 22px 0}
.desk .view-all{position:absolute;top:580px;left:0;width:1000px;text-align:center;font-family:"Oswald",sans-serif;font-size:10px;color:#ddd;text-transform:uppercase}
.view-all span{color:#fff;text-decoration:underline}

.desk .cta{position:absolute;top:2008px;left:0;width:1000px;height:211px;background:var(--red);color:#fff}
.desk .cta h2{position:absolute;left:134px;top:74px;font-size:22px}
.desk .cta p{position:absolute;left:134px;top:112px;width:430px;font-size:10px;line-height:1.7}
.btn-light{background:#fff;color:var(--red);font-family:"Oswald",sans-serif;text-transform:uppercase}
.desk .cta .btn-light{position:absolute;right:134px;top:85px;font-size:10px;padding:12px 16px}

.desk .pricing{position:absolute;top:2219px;left:0;width:1000px;height:729px;background:var(--black)}
.desk .pricing .section-title{padding-top:74px}
.desk .pricing .section-title h2{font-size:22px}
.desk .pricing .section-title p{color:#ccc;line-height:2}
.desk .price-groups{position:absolute;top:249px;left:134px;width:730px;display:grid;grid-template-columns:1fr 1fr;column-gap:37px;row-gap:20px;align-items:start}
.group h4{background:var(--red);color:#fff}
.row{display:flex;justify-content:space-between;color:#ddd;border-bottom:1px solid var(--line)}
.desk .group h4{font-size:13px;padding:10px 14px;margin-bottom:6px}
.desk .row{font-size:10px;padding:15px 0}

.desk .recognized{position:absolute;top:2948px;left:0;width:1000px;height:392px;background:#fff}
.desk .recognized-text{position:absolute;left:134px;top:75px;width:360px}
.desk .recognized-text .eyebrow{font-size:9px}
.desk .recognized-text h2{font-size:20px;margin:4px 0 14px}
.desk .recognized-text p{font-size:10px;line-height:1.8;color:var(--grey)}
.badges{display:flex}
.badge{background:#f2f2f2;display:flex;align-items:center;justify-content:center}
.desk .badges{gap:15px;margin-top:24px}
.desk .badge{width:171px;height:94px}

.desk .quote-form{position:absolute;left:547px;top:2933px;width:317px;height:418px;background:#fff;box-shadow:0 6px 22px rgba(0,0,0,.18);padding:34px 28px}
.field{border:1px solid var(--light-line);color:#999}
.desk .quote-form .eyebrow{font-size:9px}
.desk .quote-form h2{font-size:18px;margin:4px 0 20px}
.desk .field{height:28px;font-size:8.5px;padding:8px;margin-bottom:12px}
.desk .field.area{height:70px}
.desk .quote-form .btn{display:block;text-align:center;padding:11px;font-size:10px;margin-top:6px}

.desk .footer{position:absolute;top:3340px;left:0;width:1000px;height:355px;background:var(--black);color:#ddd}
.desk .foot-col{position:absolute;top:70px}
.foot-brand{font-family:"Oswald",sans-serif;font-weight:700;color:#fff;text-transform:uppercase}
.desk .foot-brand{font-size:20px}
.desk .foot-col p{font-size:10px;line-height:1.8;margin-top:18px;width:200px}
.social{display:flex}
.social span{background:#fff;display:block}
.desk .social{gap:9px;margin-top:10px}
.desk .social span{width:20px;height:20px}
.desk .foot-col h3{font-size:15px;color:#fff;margin-bottom:18px}
.hours{border-collapse:collapse}
.desk .hours{font-size:10px;line-height:2.1}
.desk .hours td:first-child{width:40px}
.contact-line{display:flex;align-items:center}
.contact-line .ic{background:var(--red);flex:none;display:flex;align-items:center;justify-content:center}
.desk .contact-line{gap:14px;font-size:9.5px;margin-bottom:20px;width:170px;line-height:1.6}
.desk .contact-line .ic{width:24px;height:24px}
.desk .copyright{position:absolute;top:3695px;left:0;width:1000px;height:42px;background:var(--red-dark);color:#fff;font-size:9.5px;text-align:center;line-height:42px}

/* ============ MOBILE PAGE (375 wide, scaled) ============ */
.mob{position:absolute;left:135px;top:945px;width:375px;height:7805px;transform:scale(.3333);transform-origin:0 0;background:#fff;overflow:hidden}
.mob .site-header{position:absolute;top:0;left:0;width:375px;height:100px;background:#fff}
.mob .brand{position:absolute;left:26px;top:32px;font-family:"Oswald",sans-serif;font-weight:700;font-size:24px;color:var(--red);text-transform:uppercase}
.mob .burger{right:26px;top:42px;width:22px;height:16px}
.mob .burger i{height:2px}
.mob .hero{position:absolute;top:100px;left:0;width:375px;height:523px;background:var(--hero)}
.mob .hero-content{position:absolute;top:132px;left:0;width:375px;padding:0 26px;text-align:center;color:#fff}
.mob .hero-content h1{font-size:30px;line-height:1.5;font-weight:500}
.mob .hero-content p{font-size:14px;line-height:1.8;margin-top:22px}
.mob .hero-content .btn{font-size:13px;padding:12px 20px;margin-top:24px}

.mob .product-tiles{position:absolute;top:654px;left:26px;width:323px}
.mob .tile{height:218px;margin-bottom:10px}
.mob .tile .photo{height:170px}
.mob .tile .label{height:48px;line-height:48px;font-size:14px}

.mob .about{position:absolute;top:1430px;left:26px;width:323px}
.mob .about-photo{height:292px;background:linear-gradient(#6f8a5a,#c9cccc 55%,#777);border:5px solid #eee;box-shadow:0 2px 8px rgba(0,0,0,.2);margin-bottom:30px}
.mob .about .eyebrow{font-size:11px}
.mob .about h2{font-size:28px;margin:4px 0 14px}
.mob .about p{font-size:12px;line-height:1.7;color:var(--grey);margin-bottom:12px}
.mob .about-cta .btn{font-size:12px;padding:13px 20px}
.mob .call{font-size:12px}
.mob .call b{font-size:14px}

.mob .services{position:absolute;top:2254px;left:0;width:375px;height:1714px;background:radial-gradient(circle at 50% 30%,#2e2d2a,#191817)}
.mob .section-title{position:absolute;top:120px;left:26px;width:323px;text-align:left}
.mob .section-title .eyebrow{font-size:11px}
.mob .section-title h2{font-size:28px;margin:4px 0 12px}
.mob .section-title p{font-size:12px;line-height:1.7;color:#aaa}
.mob .service-cards{position:absolute;top:266px;left:26px;width:323px}
.mob .service{height:423px;margin-bottom:22px}
.mob .service .photo{height:180px}
.mob .service .icon{top:150px;width:58px;height:58px;margin-left:-29px}
.mob .service h3{font-size:15px;padding-top:44px}
.mob .service p{font-size:12px;line-height:1.8;color:var(--grey);padding:12px 30px 0}
.mob .view-all{position:absolute;top:1620px;left:0;width:375px;text-align:center;font-family:"Oswald",sans-serif;font-size:12px;color:#ddd;text-transform:uppercase}

.mob .cta{position:absolute;top:3968px;left:0;width:375px;height:384px;background:var(--red);color:#fff;text-align:center;padding:80px 30px 0}
.mob .cta h2{font-size:28px;line-height:1.35}
.mob .cta p{font-size:12px;line-height:1.7;margin-top:16px}
.mob .cta .btn-light{display:inline-block;font-size:12px;padding:12px 18px;margin-top:26px}

.mob .pricing{position:absolute;top:4352px;left:0;width:375px;height:1383px;background:var(--black)}
.mob .pricing .section-title{top:118px}
.mob .pricing .section-title p{color:#ccc;line-height:1.9}
.mob .price-groups{position:absolute;top:327px;left:26px;width:323px}
.mob .group{margin-bottom:50px}
.mob .group h4{font-size:14px;padding:12px 14px;margin-bottom:8px}
.mob .row{font-size:12px;padding:18px 0}

.mob .recognized{position:absolute;top:5735px;left:0;width:375px;height:480px;background:#fff;padding:100px 26px 0}
.mob .recognized .eyebrow{font-size:11px}
.mob .recognized h2{font-size:22px;margin:4px 0 12px}
.mob .recognized p{font-size:12px;line-height:1.7;color:var(--grey)}
.mob .badges{gap:14px;margin-top:28px}
.mob .badge{width:154px;height:90px}

.mob .quote-form{position:absolute;top:6215px;left:0;width:375px;height:523px;background:#fff;padding:60px 26px 0}
.mob .quote-form .eyebrow{font-size:11px}
.mob .quote-form h2{font-size:22px;margin:4px 0 22px}
.mob .field{height:38px;font-size:11px;padding:11px 10px;margin-bottom:14px}
.mob .field.area{height:100px}
.mob .quote-form .btn{display:block;text-align:center;padding:14px;font-size:12px;margin-top:10px}

.mob .footer{position:absolute;top:6738px;left:0;width:375px;height:1003px;background:var(--black);color:#ddd;padding:60px 26px 0}
.mob .foot-brand{font-size:26px}
.mob .footer p{font-size:12px;line-height:1.7;margin-top:14px}
.mob .social{gap:12px;margin-top:12px}
.mob .social span{width:26px;height:26px}
.mob .footer h3{font-size:18px;color:#fff;margin:50px 0 16px}
.mob .hours{font-size:12px;line-height:2.3}
.mob .hours td:first-child{width:60px}
.mob .contact-line{gap:16px;font-size:12px;margin-bottom:24px;line-height:1.6}
.mob .contact-line .ic{width:30px;height:30px}
.mob .copyright{position:absolute;top:7741px;left:0;width:375px;height:64px;background:var(--red-dark);color:#fff;font-size:11px;line-height:64px;padding-left:26px}
</style>
</head>
<body>

<div class="show-brand">Harrowfield Loam</div>

<!-- flat screen previews -->
<div class="preview-desk" role="img" aria-label="Home page hero with a red excavator on a gravel site">
  <div class="p-notice">Now until further notice we will only be doing deliveries! No retail pick up at this time.</div>
  <div class="p-header">
    <div class="p-brand">Harrowfield Loam</div>
    <div class="p-nav"><span class="on">Home</span><span>About</span><span>Services</span><span>Products/Pricing</span><span>Contact</span></div>
  </div>
  <div class="p-hero">
    <div class="p-eyebrow">Welcome to Harrowfield</div>
    <h2 class="head">Landscape Supplier &amp; Excavation Services</h2>
    <p>Our emphasis is to produce the very best quality topsoil for the best results!<br>We can custom blend any products which include leaf mulch,<br>Loamwell compost and Fenwick compost to make the perfect mixtures for your needs.<br>Contractors, landscapers, nurseries, homeowners and wholesales are welcome.</p>
    <span class="btn">Our Services</span>
  </div>
</div>

<div class="preview-phone" role="img" aria-label="Mobile home page hero with a red excavator">
  <div class="p-header">
    <div class="p-brand">Harrowfield Loam</div>
    <div class="burger"><i></i><i></i><i></i></div>
  </div>
  <div class="p-hero">
    <h2 class="head">Landscape Supplier<br>&amp; Excavation Services</h2>
    <p>Our emphasis is to produce the very best quality topsoil for the best results!</p>
    <span class="btn">Our Services</span>
  </div>
</div>

<div class="side-label left">Responsive Side</div>
<div class="side-label right">Laptop / Desktop</div>

<!-- ============ MOBILE PAGE ============ -->
<div class="mob">
  <header class="site-header">
    <div class="brand">Harrowfield Loam</div>
    <div class="burger"><i></i><i></i><i></i></div>
  </header>

  <section class="hero" role="img" aria-label="Red excavator working on a gravel site">
    <div class="hero-content">
      <h1 class="head">Landscape Supplier<br>&amp; Excavation Services</h1>
      <p>Our emphasis is to produce the very best quality topsoil for the best results!</p>
      <span class="btn">Our Services</span>
    </div>
  </section>

  <div class="product-tiles">
    <div class="tile"><div class="photo" role="img" aria-label="Pile of dark topsoil" style="background:linear-gradient(#cfd5dc,#2b2a28)"></div><div class="label">Topsoil<span>&rarr;</span></div></div>
    <div class="tile"><div class="photo" role="img" aria-label="Close view of shredded mulch" style="background:linear-gradient(135deg,#6b6b6b,#3d3d3d)"></div><div class="label">Mulch<span>&rarr;</span></div></div>
    <div class="tile"><div class="photo" role="img" aria-label="Green seedlings growing in compost" style="background:linear-gradient(135deg,#3c7a1e,#9acb4a 50%,#2d4d16)"></div><div class="label">Compost<span>&rarr;</span></div></div>
  </div>

  <section class="about">
    <div class="about-photo" role="img" aria-label="White company dump truck parked by trees"></div>
    <div class="eyebrow">Introduction</div>
    <h2 class="head">About Us</h2>
    <p>Text filler for design purposes. Lorem ipsum dolor sit amet, consectetur adipiscing elit, sed do eiusmod tempor incididunt ut labore et dolore magna aliqua. Quis ipsum suspendisse ultrices gravida.</p>
    <p class="quote">“Quis autem vel eum iure reprehenderit qui in ea voluptate velit esse quam nihil molestiae consequatur, vel illum qui dolorem eum fugiat.”</p>
    <p>Sed ut perspiciatis unde omnis iste natus error sit voluptatem accusantium doloremque laudantium, totam rem aperiam, eaque ipsa quae ab illo inventore veritatis et quasi architecto beatae vitae dicta sunt explicabo.</p>
    <div class="about-cta">
      <span class="btn">Learn More</span>
      <div class="call">Call us now<br><b>555-014-2290</b></div>
    </div>
  </section>

  <section class="services">
    <div class="section-title">
      <div class="eyebrow">What we offer</div>
      <h2 class="head">Services</h2>
      <p>Text filler for design purposes. Lorem ipsum dolor sit amet, consectetur adipiscing elit, sed do eiusmod tempor incididunt ut labore et dolore magna aliqua.</p>
    </div>
    <div class="service-cards">
      <div class="service">
        <div class="photo" role="img" aria-label="Yellow excavator clearing a sandy lot" style="background:linear-gradient(#b9c7d3,#d8b25a 60%,#8a7550)"></div>
        <div class="icon"></div>
        <h3 class="head">Excavation</h3>
        <p>We provide a wide variety of excavation services, from residential to large commercial projects. We specialize in land clearing and building site preparation.</p>
      </div>
      <div class="service">
        <div class="photo" role="img" aria-label="Dump trucks unloading topsoil" style="background:linear-gradient(#c7ccd2,#e6e6e6 50%,#6e5a48)"></div>
        <div class="icon"></div>
        <h3 class="head">Topsoil</h3>
        <p>Our emphasis is to produce the very best quality topsoil for the best results! Our topsoil and organics make quality ready-made soils and lawn amendments.</p>
      </div>
      <div class="service">
        <div class="photo" role="img" aria-label="Brush pile burning during land clearing" style="background:linear-gradient(#b9b2a6,#6b5e4c 55%,#c35a2a)"></div>
        <div class="icon"></div>
        <h3 class="head">Clearing</h3>
        <p>Land clearing is the process of removing trees, stumps, brush, stones and other obstacles from an area as required for land improvement or construction projects.</p>
      </div>
    </div>
    <div class="view-all"><span>Click here to view all our services</span> &rarr;</div>
  </section>

  <section class="cta">
    <h2 class="head">Need Landscape and Excavation Services?</h2>
    <p>Lorem ipsum dolor sit amet, consectetur adipiscing elit, sed do eiusmod tempor incididunt ut labore et dolore magna aliqua.</p>
    <span class="btn-light">Contact Us</span>
  </section>

  <section class="pricing">
    <div class="section-title">
      <div class="eyebrow">Product &amp; Pricing</div>
      <h2 class="head">Products &amp; Pricing</h2>
      <p>All prices are per cubic yard.<br>Minimum delivery on most products is 14 yards, mulch is 20 yards.<br>Delivery is available at reasonable rate.<br>Retail pick up will be at Alder Springs location.</p>
    </div>
    <div class="price-groups">
      <div class="group"><h4 class="head">Topsoil</h4>
        <div class="row"><span>Unscreened Topsoil</span><span>$10</span></div>
        <div class="row"><span>Shredded Topsoil</span><span>$14</span></div>
        <div class="row"><span>Screened Topsoil</span><span>$20</span></div></div>
      <div class="group"><h4 class="head">Garden Mixes</h4>
        <div class="row"><span>Screened Topsoil &amp; 1/2 Leaf Compost</span><span>$27</span></div>
        <div class="row"><span>Screened Topsoil &amp; 1/2 Fenwick Soil Builder</span><span>$34</span></div>
        <div class="row"><span>Screened Topsoil &amp; 1/2 Fenwick Soil Builder</span><span>$34</span></div></div>
      <div class="group"><h4 class="head">Mulch</h4>
        <div class="row"><span>Double Shredded Hardwood Mulch</span><span>$15</span></div>
        <div class="row"><span>Black Dyed Mulch</span><span>$28</span></div>
        <div class="row"><span>Brown Dyed Mulch</span><span>$28</span></div></div>
      <div class="group"><h4 class="head">Compost</h4>
        <div class="row"><span>Premium Leaf Mulch</span><span>$15</span></div>
        <div class="row"><span>Fenwick Soil Builder</span><span>$15</span></div></div>
    </div>
  </section>

  <section class="recognized">
    <div class="eyebrow">Licensed &amp; Insured</div>
    <h2 class="head">Recognized by Professionals</h2>
    <p>Sed ut perspiciatis unde omnis iste natus error sit voluptatem accusantium doloremque laudantium, totam rem aperiam, eaque ipsa quae ab illo inventore.</p>
    <div class="badges">
      <div class="badge"><svg width="50" height="50"><circle cx="25" cy="25" r="22" fill="#c1282d" opacity=".8"/></svg></div>
      <div class="badge"><svg width="50" height="50"><rect x="5" y="5" width="40" height="40" fill="#222"/></svg></div>
    </div>
  </section>

  <div class="quote-form">
    <div class="eyebrow">Get in touch with us</div>
    <h2 class="head">Request a Quote</h2>
    <div class="field">Your Name*</div>
    <div class="field">Your Email Address*</div>
    <div class="field">Your Phone Number*</div>
    <div class="field area">Type Your Message*</div>
    <span class="btn">Send Your Message</span>
  </div>

  <footer class="footer">
    <div class="foot-brand">Harrowfield Loam</div>
    <p>Now until further notice we will only be doing deliveries! No retail pickup at this time.</p>
    <p style="margin-top:26px">Connect With Us:</p>
    <div class="social"><span></span><span></span></div>
    <h3 class="head">Working Hours</h3>
    <table class="hours">
      <tr><td>Mon:</td><td>08:00 am – 05:00 pm</td></tr>
      <tr><td>Tue:</td><td>08:00 am – 05:00 pm</td></tr>
      <tr><td>Wed:</td><td>08:00 am – 05:00 pm</td></tr>
      <tr><td>Thu:</td><td>08:00 am – 05:00 pm</td></tr>
      <tr><td>Fri:</td><td>08:00 am – 05:00 pm</td></tr>
      <tr><td>Sat:</td><td>09:00 am – 04:00 pm</td></tr>
      <tr><td>Sun:</td><td>Closed</td></tr>
    </table>
    <h3 class="head">Contact Us</h3>
    <div class="contact-line"><span class="ic"><svg width="14" height="14" viewBox="0 0 24 24"><path fill="#fff" d="M6.6 10.8a15 15 0 0 0 6.6 6.6l2.2-2.2c.3-.3.7-.4 1-.2 1.1.4 2.3.6 3.6.6.6 0 1 .4 1 1V20c0 .6-.4 1-1 1A17 17 0 0 1 3 4c0-.6.4-1 1-1h3.5c.6 0 1 .4 1 1 0 1.3.2 2.5.6 3.6.1.3 0 .7-.2 1z"/></svg></span>555-014-2290</div>
    <div class="contact-line"><span class="ic"><svg width="14" height="12" viewBox="0 0 24 20"><rect x="1" y="2" width="22" height="16" fill="#fff"/><path d="M1 2l11 9 11-9" stroke="#c1282d" stroke-width="2" fill="none"/></svg></span>info@pvrqx.com</div>
    <div class="contact-line"><span class="ic"><svg width="12" height="16" viewBox="0 0 24 32"><path fill="#fff" d="M12 0a11 11 0 0 0-11 11c0 8 11 21 11 21s11-13 11-21A11 11 0 0 0 12 0zm0 15a4 4 0 1 1 0-8 4 4 0 0 1 0 8z"/></svg></span>418 Brindle Road, Alder Springs,<br>Virginia 20177, United States</div>
  </footer>
  <div class="copyright">Copyright © 2021 <b>Harrowfield Loam</b> · All Rights Reserved.</div>
</div>

<!-- ============ DESKTOP PAGE ============ -->
<div class="desk">
  <div class="notice">Now until further notice we will only be doing deliveries! No retail pick up at this time.</div>
  <header class="site-header">
    <div class="brand">Harrowfield Loam</div>
    <nav class="nav"><span class="active">Home</span><span>About</span><span>Services</span><span>Products/Pricing</span><span>Contact</span></nav>
  </header>

  <section class="hero" role="img" aria-label="Red excavator working on a gravel site under a dark sky">
    <div class="hero-content">
      <div class="eyebrow">Welcome to Harrowfield</div>
      <h1 class="head">Landscape Supplier &amp; Excavation Services</h1>
      <p>Our emphasis is to produce the very best quality topsoil for the best results!<br>
      We can custom blend any products which include leaf mulch,<br>
      Loamwell compost and Fenwick compost to make the perfect mixtures for your needs.<br>
      Contractors, landscapers, nurseries, homeowners and wholesales are welcome.</p>
      <span class="btn">Our Services</span>
    </div>
  </section>

  <div class="product-tiles">
    <div class="tile"><div class="photo" role="img" aria-label="Pile of dark topsoil" style="background:linear-gradient(#cfd5dc,#2b2a28)"></div><div class="label">Topsoil<span>&rarr;</span></div></div>
    <div class="tile"><div class="photo" role="img" aria-label="Close view of shredded mulch" style="background:linear-gradient(135deg,#6b6b6b,#3d3d3d)"></div><div class="label">Mulch<span>&rarr;</span></div></div>
    <div class="tile"><div class="photo" role="img" aria-label="Green seedlings growing in compost" style="background:linear-gradient(135deg,#3c7a1e,#9acb4a 50%,#2d4d16)"></div><div class="label">Compost<span>&rarr;</span></div></div>
  </div>

  <section class="about">
    <div class="about-photo" role="img" aria-label="White company dump truck parked by trees"></div>
    <div class="about-text">
      <div class="eyebrow">Introduction</div>
      <h2 class="head">About Us</h2>
      <p>Text filler for design purposes. Lorem ipsum dolor sit amet, consectetur adipiscing elit, sed do eiusmod tempor incididunt ut labore et dolore magna aliqua. Quis ipsum suspendisse ultrices gravida.</p>
      <p class="quote">“Quis autem vel eum iure reprehenderit qui in ea voluptate velit esse quam nihil molestiae consequatur, vel illum qui dolorem eum fugiat quo voluptas nulla pariatur.”</p>
      <p>Sed ut perspiciatis unde omnis iste natus error sit voluptatem accusantium doloremque laudantium, totam rem aperiam, eaque ipsa quae ab illo inventore veritatis et quasi architecto beatae vitae dicta sunt explicabo. Nemo enim ipsam voluptatem quia voluptas sit aspernatur aut odit aut fugit.</p>
      <div class="about-cta">
        <span class="btn">Learn More</span>
        <div class="call">Call us now<br><b>555-014-2290</b></div>
      </div>
    </div>
  </section>

  <section class="services">
    <div class="section-title">
      <div class="eyebrow">What we offer</div>
      <h2 class="head">Services</h2>
      <p>Text filler for design purposes. Lorem ipsum dolor sit amet, consectetur adipiscing elit, sed do eiusmod tempor incididunt ut labore et dolore magna aliqua. Quis ipsum suspendisse ultrices gravida.</p>
    </div>
    <div class="service-cards">
      <div class="service">
        <div class="photo" role="img" aria-label="Yellow excavator clearing a sandy lot" style="background:linear-gradient(#b9c7d3,#d8b25a 60%,#8a7550)"></div>
        <div class="icon"></div>
        <h3 class="head">Excavation</h3>
        <p>We provide a wide variety of excavation services, from residential to large commercial projects. We specialize in land clearing and building site preparation.</p>
      </div>
      <div class="service">
        <div class="photo" role="img" aria-label="Dump trucks unloading topsoil" style="background:linear-gradient(#c7ccd2,#e6e6e6 50%,#6e5a48)"></div>
        <div class="icon"></div>
        <h3 class="head">Topsoil</h3>
        <p>Our emphasis is to produce the very best quality topsoil for the best results! Our topsoil and organics make quality ready-made soils and lawn amendments.</p>
      </div>
      <div class="service">
        <div class="photo" role="img" aria-label="Brush pile burning during land clearing" style="background:linear-gradient(#b9b2a6,#6b5e4c 55%,#c35a2a)"></div>
        <div class="icon"></div>
        <h3 class="head">Clearing</h3>
        <p>Land clearing is the process of removing trees, stumps, brush, stones and other obstacles from an area as required for land improvement or construction projects.</p>
      </div>
    </div>
    <div class="view-all"><span>Click here to view all our services</span> &rarr;</div>
  </section>

  <section class="cta">
    <h2 class="head">Need Landscape and Excavation Services?</h2>
    <p>Lorem ipsum dolor sit amet, consectetur adipiscing elit, sed do eiusmod tempor incididunt ut labore et dolore magna aliqua. Ut enim ad minim veniam.</p>
    <span class="btn-light">Contact Us</span>
  </section>

  <section class="pricing">
    <div class="section-title">
      <div class="eyebrow">Product &amp; Pricing</div>
      <h2 class="head">Products &amp; Pricing</h2>
      <p>All prices are per cubic yard.<br>Minimum delivery on most products is 14 yards, mulch is 20 yards.<br>Delivery is available at reasonable rate.<br>Retail pick up will be at Alder Springs location.</p>
    </div>
    <div class="price-groups">
      <div class="group"><h4 class="head">Topsoil</h4>
        <div class="row"><span>Unscreened Topsoil</span><span>$10</span></div>
        <div class="row"><span>Shredded Topsoil</span><span>$14</span></div>
        <div class="row"><span>Screened Topsoil</span><span>$20</span></div></div>
      <div class="group"><h4 class="head">Garden Mixes</h4>
        <div class="row"><span>Screened Topsoil &amp; 1/2 Leaf Compost</span><span>$27</span></div>
        <div class="row"><span>Screened Topsoil &amp; 1/2 Fenwick Soil Builder</span><span>$34</span></div>
        <div class="row"><span>Screened Topsoil &amp; 1/2 Fenwick Soil Builder</span><span>$34</span></div></div>
      <div class="group"><h4 class="head">Mulch</h4>
        <div class="row"><span>Double Shredded Hardwood Mulch</span><span>$15</span></div>
        <div class="row"><span>Black Dyed Mulch</span><span>$28</span></div>
        <div class="row"><span>Brown Dyed Mulch</span><span>$28</span></div></div>
      <div class="group"><h4 class="head">Compost</h4>
        <div class="row"><span>Premium Leaf Mulch</span><span>$15</span></div>
        <div class="row"><span>Fenwick Soil Builder</span><span>$15</span></div></div>
    </div>
  </section>

  <section class="recognized">
    <div class="recognized-text">
      <div class="eyebrow">Licensed &amp; Insured</div>
      <h2 class="head">Recognized by Professionals</h2>
      <p>Sed ut perspiciatis unde omnis iste natus error sit voluptatem accusantium doloremque laudantium, totam rem aperiam, eaque ipsa quae ab illo inventore veritatis et quasi architecto beatae vitae dicta sunt explicabo. Nemo enim ipsam voluptatem quia voluptas sit aspernatur aut odit aut fugit.</p>
      <div class="badges">
        <div class="badge"><svg width="50" height="50"><circle cx="25" cy="25" r="22" fill="#c1282d" opacity=".8"/></svg></div>
        <div class="badge"><svg width="50" height="50"><rect x="5" y="5" width="40" height="40" fill="#222"/></svg></div>
      </div>
    </div>
  </section>

  <div class="quote-form">
    <div class="eyebrow">Get in touch with us</div>
    <h2 class="head">Request a Quote</h2>
    <div class="field">Your Name*</div>
    <div class="field">Your Email Address*</div>
    <div class="field">Your Phone Number*</div>
    <div class="field area">Type Your Message*</div>
    <span class="btn">Send Your Message</span>
  </div>

  <footer class="footer">
    <div class="foot-col" style="left:134px">
      <div class="foot-brand">Harrowfield Loam</div>
      <p>Now until further notice we will only be doing deliveries! No retail pickup at this time.</p>
      <p style="margin-top:22px">Connect With Us:</p>
      <div class="social"><span></span><span></span></div>
    </div>
    <div class="foot-col" style="left:453px">
      <h3 class="head">Working Hours</h3>
      <table class="hours">
        <tr><td>Mon:</td><td>08:00 am – 05:00 pm</td></tr>
        <tr><td>Tue:</td><td>08:00 am – 05:00 pm</td></tr>
        <tr><td>Wed:</td><td>08:00 am – 05:00 pm</td></tr>
        <tr><td>Thu:</td><td>08:00 am – 05:00 pm</td></tr>
        <tr><td>Fri:</td><td>08:00 am – 05:00 pm</td></tr>
        <tr><td>Sat:</td><td>09:00 am – 04:00 pm</td></tr>
        <tr><td>Sun:</td><td>Closed</td></tr>
      </table>
    </div>
    <div class="foot-col" style="left:697px">
      <h3 class="head">Contact Us</h3>
      <div class="contact-line"><span class="ic"><svg width="12" height="12" viewBox="0 0 24 24"><path fill="#fff" d="M6.6 10.8a15 15 0 0 0 6.6 6.6l2.2-2.2c.3-.3.7-.4 1-.2 1.1.4 2.3.6 3.6.6.6 0 1 .4 1 1V20c0 .6-.4 1-1 1A17 17 0 0 1 3 4c0-.6.4-1 1-1h3.5c.6 0 1 .4 1 1 0 1.3.2 2.5.6 3.6.1.3 0 .7-.2 1z"/></svg></span>555-014-2290</div>
      <div class="contact-line"><span class="ic"><svg width="12" height="10" viewBox="0 0 24 20"><rect x="1" y="2" width="22" height="16" fill="#fff"/><path d="M1 2l11 9 11-9" stroke="#c1282d" stroke-width="2" fill="none"/></svg></span>info@pvrqx.com</div>
      <div class="contact-line"><span class="ic"><svg width="10" height="14" viewBox="0 0 24 32"><path fill="#fff" d="M12 0a11 11 0 0 0-11 11c0 8 11 21 11 21s11-13 11-21A11 11 0 0 0 12 0zm0 15a4 4 0 1 1 0-8 4 4 0 0 1 0 8z"/></svg></span>418 Brindle Road, Alder Springs, Virginia 20177, United States</div>
    </div>
  </footer>
  <div class="copyright">Copyright © 2021 <b>Harrowfield Loam</b> · All Rights Reserved.</div>
</div>

</body>
</html>
```